Technical Communications firm needs an article turned into a white paper

We want to redesign a 3-part blog series into a white paper that we can print for a conference. I've consolidated the three posts into the attached Word document.

We are looking for a light, easy to read design. Good use of graphics to support the message. I've added the graphics we used in the original post.

You can view them at
http://www.quillmarrowgroup.com/blog/are-you-satisfied-with-your-dita-solution/

Target Market(s)

Product managers from High-tech, Finance, and Medical industries.

Industry/Entity Type

Information Technology

Colors

Designer to choose colors to be used in the design.

Requirements
Must have
• Must be modern, light, easy to read and slick design. Try to incorporate the graphics provided, but feel free to add more. Must retain the lists and tables.
• Must align with our website/brand.
• Must be easy to read. So not too busy.
• Please move all footnotes to endnotes. You'll need to rework the numbering.
Nice to have
• Awesome coverpage.
Should not have
• Hokey clipart. Not too heavy or hard to read.

```html
<!DOCTYPE html>
<html lang="en">
<head>
<meta charset="utf-8">
<title>Are You Satisfied With Your DITA Solution?</title>
<link rel="stylesheet" href="https://fonts.googleapis.com/css2?family=Lato:wght@400;700&family=Orbitron:wght@500;700;800&display=swap">
<style>
  :root {
    --navy: #1a1f9c;
    --navy-deep: #141a86;
    --cyan: #19b4ec;
    --ink: #3b3b3b;
    --heading: #14197a;
    --band: #efefef;
    --box-light: #d9d9d9;
    --box-mid: #a8a8a8;
    --foot: #7b7b7b;
    --canvas: #d6d6d6;
    --white: #ffffff;
  }
  * { box-sizing: border-box; margin: 0; padding: 0; }
  html, body { width: 1200px; height: 1200px; overflow: hidden; }
  body { background: var(--canvas); font-family: "Lato", sans-serif; color: var(--ink); }
  .page { position: absolute; left: 180px; top: 10px; width: 840px; height: 1180px; background: var(--white); overflow: hidden; }

  .header { position: absolute; left: 0; top: 0; width: 840px; height: 122px; }
  .brand { position: absolute; left: 42px; top: 38px; display: flex; align-items: center; gap: 10px; }
  .brand-dot { width: 46px; height: 46px; border-radius: 50%; background: var(--navy); }
  .brand-name { font-weight: 700; font-size: 23px; color: var(--navy); line-height: 1; }
  .contact { position: absolute; right: 42px; top: 34px; list-style: none; font-size: 16px; color: var(--ink); }
  .contact li { display: flex; align-items: center; gap: 10px; height: 26px; }
  .contact svg { width: 13px; height: 13px; }

  .hero { position: absolute; left: 0; top: 122px; width: 840px; height: 266px; }
  .hero-image { position: absolute; inset: 0; background: linear-gradient(135deg, #e9eef3 0%, #c9d3dc 45%, #7d93aa 70%, #b9c3cc 100%); }
  .hero-panel { position: absolute; inset: 0; }
  .hero-title { position: absolute; right: 40px; top: 18px; text-align: right; font-family: "Orbitron", sans-serif; }
  .hero-title .soft { display: block; font-family: "Lato", sans-serif; color: var(--white); font-size: 36px; line-height: 42px; }
  .hero-title .soft.small { font-size: 30px; line-height: 36px; font-weight: 700; }
  .hero-title .strong { display: block; color: var(--cyan); font-weight: 800; font-size: 37px; line-height: 42px; }
  .hero-title .strong.big { font-size: 44px; line-height: 52px; }
  .hero-title .tag { display: inline-block; margin-top: 6px; background: var(--white); color: var(--navy); font-weight: 800; font-size: 25px; padding: 4px 12px; }

  .intro { position: absolute; left: 37px; top: 405px; width: 770px; font-size: 13.4px; line-height: 16.5px; }
  .intro .byline { font-weight: 700; }

  .issues { position: absolute; left: 0; top: 557px; width: 840px; height: 223px; background: var(--band); padding: 10px 37px 0; }
  .section-title { font-family: "Orbitron", sans-serif; font-weight: 700; color: var(--heading); font-size: 14.5px; letter-spacing: 0.3px; }
  .section-text { font-size: 13.4px; line-height: 16.5px; margin-top: 6px; }
  .categories { display: flex; justify-content: space-between; margin: 17px 0 14px; padding: 0 40px 0 10px; }
  .category { width: 160px; text-align: center; font-size: 13.4px; font-weight: 700; }
  .category:nth-child(1) { margin-left: -12px; }
  .category svg { display: block; margin: 0 auto 17px; width: 56px; height: 56px; }

  .article { position: absolute; left: 37px; top: 792px; width: 780px; }
  .parts { position: absolute; left: 0; top: 849px; width: 840px; }
  .part-label { position: absolute; left: 43px; font-family: "Orbitron", sans-serif; font-weight: 700; font-size: 14.5px; color: #333; display: flex; align-items: center; gap: 12px; }
  .part-label::before { content: ""; width: 7px; height: 7px; border-radius: 50%; background: var(--navy); }
  .part-box { position: absolute; left: 360px; width: 480px; padding: 8px 34px 0 20px; font-size: 13.4px; line-height: 16.5px; }
  .part-box.light { background: var(--box-light); color: var(--ink); }
  .part-box.mid { background: var(--box-mid); color: var(--white); }

  .footnotes { position: absolute; left: 0; top: 1104px; width: 840px; height: 62px; background: var(--foot); color: var(--white); padding: 8px 37px 0; font-size: 10px; line-height: 13px; }
</style>
</head>
<body>
<div class="page">
  <header class="header">
    <div class="brand"><span class="brand-dot"></span><span class="brand-name">Quillmarrow Group</span></div>
    <ul class="contact">
      <li><svg viewBox="0 0 16 16"><path d="M3 1l3 3-1.5 2a9 9 0 005 5L11.5 9.5l3 3-2 2C7 15 1 9 1.5 3z" fill="#1a1f9c"/></svg>1 (555) 014-7720</li>
      <li><svg viewBox="0 0 16 16"><circle cx="8" cy="8" r="6.5" fill="none" stroke="#1a1f9c" stroke-width="1.6"/><path d="M1.5 8h13M8 1.5c-3 3-3 10 0 13M8 1.5c3 3 3 10 0 13" fill="none" stroke="#1a1f9c" stroke-width="1.2"/></svg>www.quillmarrowgroup.com</li>
      <li><svg viewBox="0 0 16 16"><rect x="1" y="4" width="14" height="10" fill="#1a1f9c"/><path d="M1 4l7 6 7-6" fill="none" stroke="#fff" stroke-width="1.2"/></svg>info@quillmarrowgroup.com</li>
    </ul>
  </header>

  <section class="hero">
    <div class="hero-image" role="img" aria-label="Photo of hands holding a red gear puzzle piece beside a head made of blue gears against a cloudy sky"></div>
    <svg class="hero-panel" viewBox="0 0 840 266" preserveAspectRatio="none"><polygon points="452,0 840,0 840,266 544,266" fill="#1a1f9c"/><polygon points="500,0 452,0 544,266 514,266" fill="#ffffff"/></svg>
    <h1 class="hero-title">
      <span class="soft">Are You</span>
      <span class="strong">SATISFIED</span>
      <span class="soft small">With Your</span>
      <span class="strong big">DITA</span>
      <span class="tag">SOLUTION?</span>
    </h1>
  </section>

  <section class="intro">
    <p class="byline">By Dana Whitcombe – President of Quillmarrow Authoring Group Inc.</p>
    <p>If your answer is “No” then you are not alone according to a 2017 survey of more than 250 technical communication professionals conducted by The Docs Roundup. The DITA Satisfaction Survey[i] indicates that 62% of respondents using DITA are—to varying degrees—dissatisfied. As many as 10% of that group were very dissatisfied reporting that their DITA implementation is experiencing ‘big’ challenges. It’s not surprising that there’s significant dissatisfaction amongst those who have adopted DITA. After all, moving to DITA is a seismic shift in technical writing; a big change with many opportunities for things to go wrong.</p>
    <p>The good news is that most DITA users don’t see their problems as insurmountable. Many just need a little help getting to where they’d like to be.</p>
  </section>

  <section class="issues">
    <h2 class="section-title">Breakdown of the issues</h2>
    <p class="section-text">The Docs Roundup DITA Satisfaction Survey asked respondents to rank the top 10 issues facing DITA users. These issues fit into three major categories including</p>
    <div class="categories">
      <div class="category">
        <svg viewBox="0 0 56 56"><circle cx="28" cy="28" r="27" fill="#1a1f9c"/><circle cx="28" cy="28" r="23" fill="none" stroke="#fff" stroke-width="1.5"/><circle cx="28" cy="28" r="5" fill="none" stroke="#fff" stroke-width="1.5"/><g fill="#fff"><circle cx="28" cy="15" r="2.5"/><circle cx="40" cy="24" r="2.5"/><circle cx="36" cy="39" r="2.5"/><circle cx="20" cy="39" r="2.5"/><circle cx="16" cy="24" r="2.5"/></g><path d="M28 17v6M38 25l-5 2M35 37l-4-5M21 37l4-5M18 25l5 2" stroke="#fff" stroke-width="1.2"/></svg>
        Skills Development
      </div>
      <div class="category">
        <svg viewBox="0 0 56 56"><circle cx="28" cy="28" r="27" fill="#1a1f9c"/><circle cx="28" cy="28" r="23" fill="none" stroke="#fff" stroke-width="1.5"/><rect x="15" y="16" width="26" height="18" rx="1.5" fill="#fff"/><rect x="18" y="19" width="20" height="12" fill="#1a1f9c"/><rect x="25" y="34" width="6" height="4" fill="#fff"/><rect x="20" y="38" width="16" height="2.5" fill="#fff"/></svg>
        Technology
      </div>
      <div class="category">
        <svg viewBox="0 0 56 56"><circle cx="28" cy="28" r="27" fill="#1a1f9c"/><circle cx="28" cy="28" r="23" fill="none" stroke="#fff" stroke-width="1.5"/><circle cx="24" cy="17" r="3.5" fill="#fff"/><rect x="20" y="22" width="8" height="18" rx="2" fill="#fff"/><rect x="30" y="30" width="9" height="9" fill="#fff"/><circle cx="34.5" cy="29" r="2.2" fill="#fff"/><circle cx="40" cy="34.5" r="2.2" fill="#fff"/></svg>
        Management
      </div>
    </div>
    <p class="section-text">The DITA Satisfaction Survey Aggregate Results revealed little spread between the ranking of the issues indicating that respondents likely faced more than one issue of concern.</p>
  </section>

  <section class="article">
    <h2 class="section-title">In this article</h2>
    <p class="section-text">In this article, we examine three issues impacting DITA satisfaction to help you find the best place to start making improvements</p>
  </section>

  <section class="parts">
    <div class="part-label" style="top:17px">Part 1: Skills Development</div>
    <div class="part-box light" style="top:0;height:68px">This problem area is far and away the most pressing obstacle for a successful DITA deployment. Too often authors are left to figure out how to adapt to writing for DITA on their own.</div>
    <div class="part-label" style="top:99px">Part 2: Technology</div>
    <div class="part-box mid" style="top:71px;height:66px">We often hear about the failure of the technology as it relates to performance or complexity. While technology may seem the most likely culprit, it is often not the root cause of the problem.</div>
    <div class="part-label" style="top:191px">Part 3: Management</div>
    <div class="part-box light" style="top:141px;height:96px">While these issues appear to be of least concern to many survey respondents, they are most likely to form the root cause of all other issues identified in the survey. This points to a general lack of awareness as to the role management should be playing in collaborative, structured authoring solutions.</div>
  </section>

  <footer class="footnotes">
    <p>FOOT NOTES (Intro)</p>
    <p>[i] DITA Satisfaction Survey published by The Docs Roundup on May 31, 2017. Listen to an analysis of the results by Dana Whitcombe, Elliot Varga-Simmons, Nora Pell, and Tobias Reyne and download a copy of the results today from StreamForum at https://www.streamforum.net/webcast/9273/259775</p>
  </footer>
</div>
</body>
</html>
```